Paperback Book Cover Design

I need a professional cover designed for my new book. You must use the design template enclosed. The title of the book is “Begin Building Wealth From Home Now!” The graphic used on the book cover should of course relate to making money online through various skills such as writing, graphic design, online marketing, photography, trading, Vendora etc. The graphic(s) used must demonstrate to the reader that the book gives various ways to make money online.

At the top of the book you must include the sub heading “Earn Cash From Home Series”. The main title of the book is “Begin Building Wealth From Home Now!”, which of course should be highly prominent on the front cover. The front cover must also include the author name, Gerald Finchley.

I have no preference to colours used so do be creative to create an eye catching cover design.

The spine of the book should include the main title and the author name. Feel free to use an image or images for the rear of the book and just add dummy text.

The winning designer must supply a layered psd file complete with all fonts and elements used.
Updates

Industry/Entity Type

Graphic Design

Requirements
Must have
• The winning designer must supply a layered psd file complete with all fonts and elements used.

```html
<!DOCTYPE html>
<html lang="en">
<head>
<meta charset="utf-8">
<title>Begin Building Wealth From Home Now! – Cover Spread</title>
<link href="https://fonts.googleapis.com/css2?family=Anton&family=Cinzel:wght@500&family=Permanent+Marker&family=Questrial&display=swap" rel="stylesheet">
<style>
  :root {
    --page-bg: #ffffff;
    --title-green-light: #4cff3a;
    --title-green: #22d11c;
    --title-green-dark: #0e7a0c;
    --accent-yellow: #ffd21a;
    --accent-yellow-dark: #b38a00;
    --ink: #1c1c1c;
    --ink-soft: #3a3a3a;
    --frame-white: #ffffff;
    --photo-light: #ececec;
    --photo-skin: #d8b39a;
    --photo-mid: #bdbdbd;
    --photo-dark: #262626;
  }
  * { box-sizing: border-box; margin: 0; padding: 0; }
  html, body {
    width: 1200px; height: 1000px; overflow: hidden;
    background: var(--page-bg);
  }
  .spread {
    position: absolute; left: 50px; top: 120px;
    width: 1100px; height: 760px;
    display: flex; overflow: hidden;
    box-shadow: 0 6px 18px rgba(0,0,0,.35);
  }
  .cover-photo {
    position: absolute; inset: 0;
    background:
      radial-gradient(ellipse 30% 40% at 20% 30%, rgba(216,179,154,.9), transparent 70%),
      radial-gradient(ellipse 28% 45% at 78% 40%, rgba(216,179,154,.85), transparent 70%),
      linear-gradient(170deg, var(--photo-light) 0%, var(--photo-skin) 35%, var(--photo-mid) 55%, #6a6a6a 72%, var(--photo-dark) 92%);
  }
  .back-cover, .spine, .front-cover { position: relative; height: 100%; }
  .back-cover { width: 506px; }
  .spine { width: 100px; }
  .front-cover { width: 494px; }

  /* back cover */
  .back-veil {
    position: absolute; left: 150px; top: 16px; width: 340px; height: 250px;
    background: rgba(255,255,255,.55);
  }
  .back-blurb {
    position: absolute; left: 160px; top: 24px; width: 320px;
    columns: 2; column-gap: 14px;
    font: 10.5px/1.35 "Questrial", sans-serif; color: var(--ink-soft);
    text-align: justify;
  }
  .back-badge { position: absolute; left: 12px; top: 14px; width: 128px; }
  .back-badge .series-line { font-size: 11px; }
  .back-badge .title-frame { margin-top: 4px; padding: 4px 10px; }
  .back-badge .title-main { font-size: 21px; }
  .back-badge .title-now { font-size: 18px; right: 2px; bottom: -16px; }

  /* shared type */
  .series-line {
    font-family: "Questrial", sans-serif; color: var(--ink);
    white-space: nowrap;
  }
  .title-frame { position: relative; }
  .title-frame::before, .title-frame::after {
    content: ""; position: absolute; top: 0; bottom: 0; width: 14%;
    border: 0 solid var(--frame-white);
  }
  .title-frame::before { left: 0; border-width: 10px 0 10px 10px; }
  .title-frame::after { right: 0; border-width: 10px 10px 10px 0; }
  .back-badge .title-frame::before { border-width: 3px 0 3px 3px; }
  .back-badge .title-frame::after { border-width: 3px 3px 3px 0; }
  .title-main {
    font-family: "Anton", sans-serif; text-transform: uppercase;
    text-align: center; line-height: .98; letter-spacing: -.5px;
    background: linear-gradient(180deg, var(--title-green-light), var(--title-green) 55%, var(--title-green-dark));
    -webkit-background-clip: text; background-clip: text; color: transparent;
    filter: drop-shadow(1px 2px 1px rgba(0,0,0,.55));
  }
  .title-now {
    position: absolute; font-family: "Permanent Marker", cursive;
    color: var(--accent-yellow); transform: rotate(-14deg);
    text-shadow: 1px 2px 0 var(--accent-yellow-dark), 2px 3px 3px rgba(0,0,0,.5);
    white-space: nowrap;
  }

  /* spine */
  .spine-titles {
    position: absolute; top: 14px; left: 12px; height: 640px;
    writing-mode: vertical-rl; display: flex; gap: 6px;
  }
  .spine .series-line { font-size: 15px; }
  .spine-title {
    font-family: "Anton", sans-serif; text-transform: uppercase; font-size: 27px;
    color: var(--title-green); line-height: 1.05;
    text-shadow: 1px 1px 1px rgba(0,0,0,.6); white-space: nowrap;
  }
  .spine-author {
    position: absolute; bottom: 22px; left: 0; width: 100%;
    text-align: center; font: 500 11px/1.25 "Cinzel", serif; color: var(--ink);
  }

  /* front cover */
  .front-cover .series-line {
    position: absolute; top: 18px; left: 0; width: 100%;
    text-align: center; font-size: 30px;
  }
  .front-cover .title-frame {
    position: absolute; left: 26px; top: 80px; width: 444px; height: 520px;
    padding: 32px 24px;
  }
  .front-cover .title-main { font-size: 88px; }
  .front-cover .title-now { font-size: 72px; right: 6px; bottom: -40px; }
  .front-author {
    position: absolute; bottom: 34px; left: 0; width: 100%;
    text-align: center; font: 500 28px "Cinzel", serif; color: var(--ink);
    letter-spacing: 1px;
  }
</style>
</head>
<body>
<main class="spread">
  <div class="cover-photo" role="img" aria-label="Photo of hands typing on a computer keyboard to earn money online, blurred, running across the whole cover"></div>

  <section class="back-cover">
    <div class="back-badge">
      <p class="series-line">Earn Cash From Home Series:</p>
      <div class="title-frame">
        <h2 class="title-main">Begin<br>Building<br>Wealth<br>From Home</h2>
        <span class="title-now">Now!</span>
      </div>
    </div>
    <div class="back-veil"></div>
    <p class="back-blurb">Discover practical ways to earn from your own desk. This guide walks you through freelance writing, graphic design, online marketing, photography, trading and selling on Vendora. Each chapter offers clear steps, real tips and simple tools you can use today. Learn how to find clients, price your work, build a portfolio and grow a steady income without leaving home. Whether you want extra cash or a full career, these proven methods help you start fast and keep going.</p>
  </section>

  <section class="spine">
    <div class="spine-titles">
      <p class="series-line">Earn Cash From Home Series:</p>
      <p class="spine-title">Begin Building Wealth From Home Now</p>
    </div>
    <p class="spine-author">By:<br>Gerald<br>Finchley</p>
  </section>

  <section class="front-cover">
    <p class="series-line">Earn Cash From Home Series:</p>
    <div class="title-frame">
      <h1 class="title-main">Begin<br>Building<br>Wealth<br>From Home</h1>
      <span class="title-now">Now!</span>
    </div>
    <p class="front-author">By: Gerald Finchley</p>
  </section>
</main>
</body>
</html>
```